New Bicycle shop business card

Hi!
I'm looking for a business card for my new proffesional bike mechanics shop. This shop is only for fixing broken bikes and not selling bikes.
Peferbly a modern and sleek and modern design.
Colors: black, grey, red, white
Information:
Name: Rijwielwerkplaats Vanhoutem
Shop owner: Bart Vanhoutem & Sanne Maertens
Website: www.rijwielwerkplaats-vanhoutem.be
Email: info@rijwielwerkplaats-vanhoutem.be
Phone number: +32471902386
Street adres: Kerkweg 64
9970 Oostmoere
Slogan/shop information: Herstellingen van alle merken.
Logo: see files.
Target Market(s)
People who seek a mechanic to fix or upgrade their bikes.
Contact Information for Business Card
Information:
Website: info@rijwielwerkplaats-vanhoutem.be
9970 Oostmoere
Logo: see files.

```html
<!DOCTYPE html>
<html lang="nl">
<head>
<meta charset="utf-8">
<title>Rijwielwerkplaats Vanhoutem – Visitekaartje</title>
<link rel="stylesheet" href="https://fonts.googleapis.com/css2?family=Lato:wght@400;700;900&display=swap">
<style>
  :root {
    --page: #dcdcdc;
    --card-white: #fcf7f7;
    --ink: #1f1a19;
    --ink-soft: #3a3434;
    --brand-red: #e3173e;
    --back-dark: #1d1412;
    --back-pattern: #2a201d;
    --divider: #9a9494;
    --white: #ffffff;
  }
  * { box-sizing: border-box; margin: 0; padding: 0; }
  html, body {
    width: 1200px; height: 782px; overflow: hidden;
    background: var(--page);
    font-family: "Lato", Arial, sans-serif;
  }
  .sheet {
    position: relative; width: 1200px; height: 782px;
    display: flex; align-items: center; justify-content: center; gap: 40px;
  }
  .card {
    position: relative; width: 540px; height: 349px; overflow: hidden;
    box-shadow: 0 6px 18px rgba(0,0,0,.18);
  }

  /* Front */
  .card--front { background: var(--card-white); }
  .brand {
    position: absolute; left: 26px; top: 96px; width: 230px;
    display: flex; flex-direction: column; align-items: center; text-align: center;
  }
  .brand__dot {
    width: 42px; height: 42px; border-radius: 50%;
    background: var(--brand-red); margin-bottom: 12px;
  }
  .brand__name {
    font-weight: 900; font-size: 19px; line-height: 1.2;
    letter-spacing: 1.5px; text-transform: uppercase; color: var(--ink);
  }
  .divider {
    position: absolute; left: 272px; top: 96px; width: 1px; height: 120px;
    background: var(--divider);
  }
  .contact {
    position: absolute; left: 290px; top: 96px; right: 14px;
    color: var(--ink); font-size: 13px; line-height: 1.45;
  }
  .contact__names {
    color: var(--brand-red); font-weight: 700; font-size: 13px;
    text-transform: uppercase; letter-spacing: .3px; line-height: 1.25;
  }
  .contact__role { font-size: 12.5px; color: var(--ink-soft); margin-bottom: 4px; }
  .contact__row { display: flex; align-items: center; gap: 6px; white-space: nowrap; }
  .contact__icon { width: 11px; height: 11px; flex: none; fill: var(--brand-red); }
  .contact__address { margin-top: 3px; }
  .band { position: absolute; left: 0; bottom: 0; width: 540px; height: 70px; }

  /* Back */
  .card--back { background: var(--back-dark); }
  .back__pattern {
    position: absolute; inset: 0;
    background: radial-gradient(circle at 50% 45%, var(--back-pattern), var(--back-dark) 75%);
  }
  .back__mark {
    position: absolute; left: 0; right: 0; top: 118px;
    display: flex; align-items: center; justify-content: center; gap: 10px;
  }
  .back__square { width: 22px; height: 22px; background: var(--brand-red); }
  .back__name {
    font-weight: 900; font-size: 16px; letter-spacing: 1.5px;
    text-transform: uppercase; color: var(--brand-red);
  }
  .back__slogan {
    position: absolute; left: 0; right: 0; top: 196px; text-align: center;
    color: var(--white); font-size: 15px; letter-spacing: 1px; text-transform: uppercase;
  }
</style>
</head>
<body>
<main class="sheet">

  <section class="card card--front" aria-label="Voorkant visitekaartje">
    <div class="brand">
      <span class="brand__dot"></span>
      <p class="brand__name">Rijwielwerkplaats<br>Vanhoutem</p>
    </div>

    <span class="divider"></span>

    <div class="contact">
      <p class="contact__names">Bart Vanhoutem &amp; Sanne Maertens</p>
      <p class="contact__role">Owner</p>
      <p class="contact__row">
        <svg class="contact__icon" viewBox="0 0 24 24"><path d="M6.6 10.8a15 15 0 0 0 6.6 6.6l2.2-2.2a1 1 0 0 1 1-.25 11.4 11.4 0 0 0 3.6.57 1 1 0 0 1 1 1V20a1 1 0 0 1-1 1A17 17 0 0 1 3 4a1 1 0 0 1 1-1h3.5a1 1 0 0 1 1 1c0 1.25.2 2.45.57 3.57a1 1 0 0 1-.25 1z"/></svg>
        +32471902386
      </p>
      <p class="contact__row">
        <svg class="contact__icon" viewBox="0 0 24 24"><path d="M2 5h20v14H2z M2 5l10 8 10-8" fill="var(--brand-red)"/><path d="M3 6l9 7 9-7" stroke="var(--card-white)" stroke-width="2" fill="none"/></svg>
        info@rijwielwerkplaats-vanhoutem.be
      </p>
      <p class="contact__row">
        <svg class="contact__icon" viewBox="0 0 24 24"><circle cx="12" cy="12" r="11"/><path d="M1 12h22M12 1c4 4 4 18 0 22M12 1c-4 4-4 18 0 22" stroke="var(--card-white)" stroke-width="1.6" fill="none"/></svg>
        www.rijwielwerkplaats-vanhoutem.be
      </p>
      <p class="contact__address">Kerkweg 64<br>9970 Oostmoere</p>
    </div>

    <svg class="band" viewBox="0 0 540 70" preserveAspectRatio="none" aria-hidden="true">
      <polygon points="0,0 275,0 250,30 0,30" fill="var(--ink)"/>
      <polygon points="250,30 540,30 540,70 0,70 0,30" fill="none"/>
      <polygon points="258,32 540,32 540,70 225,70" fill="var(--brand-red)"/>
    </svg>
  </section>

  <section class="card card--back" aria-label="Achterkant visitekaartje">
    <div class="back__pattern" role="img" aria-label="Subtiel herhaald merkpatroon op donkere achtergrond"></div>
    <div class="back__mark">
      <span class="back__square"></span>
      <span class="back__name">Rijwielwerkplaats Vanhoutem</span>
    </div>
    <p class="back__slogan">Herstellingen van alle merken</p>
  </section>

</main>
</body>
</html>
```